Business card for dental office with laser therapy / dental facial esthetic

A simple logo which should signifies
Dentistry intraoral as primary and with extended extraoral cosmetic facial esthetic services ( regenerative skincare ) which enhance Beauty as whole .
Conservative high tech approach by using laser intraoral and extraoral limited to face and neck
Front Face :May be black background with neon blue / purplish Rim signifies laser ( ?) & abstract face profile and tooth or Apple design in one ? / see upload inspiration design
Back side : simple appointment slots with date and time / white background / black letter

Color : black/ neon blue/ purplish and gold incorporate for logo design
Final design : dental / esthetic / modern high tech and safe

Target Market(s)

Dental Patients who seeks more high end cosmetic treatment

Industry/Entity Type

Health Care

Contact Information for Business Card

Esthetic modern elegant looking
Logo and office must haves important informations

Logo Text

Family & Cosmetic Dentistry

Font styles to use
Script

Requirements
Must have
• Name of practice and all important informations
• Family & Cosmetic Dentistry
• Lan B. Okafor DMD,PC
• 38412 Brantley Court ,ste.207
• Cedar Hollow ,VA 20391
• Ph. 703-555-0187
• Fax 703-5550193
Nice to have
• More abstract
• Front : black back ground with neon blue rim (signifies laser therapy)
• Logo can also be golden gold / neon blue
• Address & Infos can be white
Should not have
• Not to busy looking

```html
<!DOCTYPE html>
<html lang="en">
<head>
<meta charset="utf-8">
<title>Family &amp; Cosmetic Dentistry – Business Card</title>
<link href="https://fonts.googleapis.com/css2?family=Playball&family=Quicksand:wght@500;600&family=Roboto:wght@400;500;700&display=swap" rel="stylesheet">
<style>
  :root {
    --stage: #2a2a2c;
    --card-dark: #0d0d0f;
    --card-dark-2: #1e1e22;
    --card-light: #f4f5f7;
    --card-light-2: #dfe1e5;
    --laser-blue: #4a63d8;
    --gold: #e9c63a;
    --aqua: #63c9d6;
    --ink: #111111;
    --rule: #6d6f73;
    --white: #ffffff;
  }
  * { box-sizing: border-box; margin: 0; padding: 0; }
  html, body { width: 1200px; height: 1200px; overflow: hidden; }
  body {
    background: var(--stage);
    display: flex;
    flex-direction: column;
    align-items: center;
    justify-content: center;
    gap: 44px;
    font-family: "Roboto", Arial, sans-serif;
  }
  .card {
    position: relative;
    width: 900px;
    height: 514px;
    border-radius: 26px;
    overflow: hidden;
  }

  /* Back: appointment card */
  .card--back {
    background: linear-gradient(135deg, var(--card-light) 0%, var(--white) 40%, var(--card-light-2) 70%, var(--card-light) 100%);
    color: var(--ink);
  }
  .appointment__title {
    position: absolute;
    left: 72px;
    top: 52px;
    font-weight: 700;
    font-size: 22px;
  }
  .appointment__slots {
    position: absolute;
    left: 72px;
    right: 60px;
    top: 118px;
    list-style: none;
  }
  .appointment__slot {
    position: relative;
    height: 62px;
    border-bottom: 1.5px solid var(--rule);
  }
  .appointment__slot::before,
  .appointment__slot::after {
    content: "/";
    position: absolute;
    bottom: 4px;
    font-size: 24px;
    color: var(--ink);
  }
  .appointment__slot::before { left: 52%; }
  .appointment__slot::after { left: 78%; }

  /* Front: practice card */
  .card--front {
    background: radial-gradient(ellipse at 50% 45%, var(--card-dark-2) 0%, var(--card-dark) 70%);
    color: var(--white);
    text-align: center;
  }
  .laser-rims {
    position: absolute;
    inset: 0;
    width: 100%;
    height: 100%;
  }
  .front__content {
    position: relative;
    padding-top: 44px;
  }
  .brand {
    display: flex;
    align-items: center;
    justify-content: center;
    gap: 14px;
  }
  .brand__dot {
    width: 58px;
    height: 58px;
    border-radius: 50%;
    background: var(--gold);
  }
  .brand__name {
    font-family: "Playball", cursive;
    font-size: 62px;
    color: var(--gold);
    margin-top: 10px;
    line-height: 1.1;
  }
  .tagline {
    font-family: "Quicksand", sans-serif;
    font-weight: 500;
    font-size: 24px;
    color: var(--aqua);
    letter-spacing: 0.5px;
  }
  .doctor {
    font-weight: 700;
    font-size: 26px;
    margin-top: 22px;
  }
  .divider {
    width: 18px;
    height: 2px;
    background: var(--white);
    margin: 10px auto;
  }
  .address { font-size: 22px; }
  .contact {
    list-style: none;
    font-size: 23px;
    line-height: 1.4;
  }
  .contact__item {
    display: flex;
    align-items: center;
    justify-content: center;
    gap: 10px;
  }
  .contact__icon { width: 22px; height: 22px; flex: none; }
  .contact__circle {
    width: 18px;
    height: 18px;
    border-radius: 50%;
    border: 2px solid var(--gold);
  }
</style>
</head>
<body>

  <section class="card card--back" aria-label="Appointment card">
    <h2 class="appointment__title">Appointment</h2>
    <ul class="appointment__slots">
      <li class="appointment__slot"></li>
      <li class="appointment__slot"></li>
      <li class="appointment__slot"></li>
      <li class="appointment__slot"></li>
      <li class="appointment__slot"></li>
    </ul>
  </section>

  <section class="card card--front" aria-label="Practice card">
    <svg class="laser-rims" viewBox="0 0 900 514" aria-hidden="true">
      <g fill="none" stroke="var(--laser-blue)" stroke-width="4">
        <ellipse cx="450" cy="257" rx="395" ry="330"/>
        <ellipse cx="450" cy="257" rx="330" ry="300"/>
      </g>
    </svg>
    <div class="front__content">
      <div class="brand">
        <span class="brand__dot" aria-hidden="true"></span>
      </div>
      <h1 class="brand__name">Family &amp; Cosmetic Dentistry</h1>
      <p class="tagline">Laser therapy / Dental facial Aesthetics</p>
      <p class="doctor">Lan B. Okafor DMD,PC</p>
      <div class="divider"></div>
      <p class="address">38412 Brantley Court ste207 , Cedar Hollow , VA 20391</p>
      <div class="divider"></div>
      <ul class="contact">
        <li class="contact__item">
          <svg class="contact__icon" viewBox="0 0 24 24" aria-hidden="true"><path fill="var(--gold)" d="M6.6 10.8a15.1 15.1 0 0 0 6.6 6.6l2.2-2.2c.3-.3.7-.4 1-.2 1.1.4 2.3.6 3.6.6.6 0 1 .4 1 1V20c0 .6-.4 1-1 1A17 17 0 0 1 3 4c0-.6.4-1 1-1h3.5c.6 0 1 .4 1 1 0 1.3.2 2.5.6 3.6.1.3 0 .7-.2 1z"/></svg>
          703-555-0187
        </li>
        <li class="contact__item">
          <svg class="contact__icon" viewBox="0 0 24 24" aria-hidden="true"><rect x="2" y="5" width="20" height="14" rx="1" fill="var(--gold)"/><path d="M2 6l10 7 10-7" fill="none" stroke="var(--card-dark)" stroke-width="1.6"/></svg>
          cedarfacialstudio.com
        </li>
        <li class="contact__item">
          <span class="contact__circle" aria-hidden="true"></span>
          dentistlan
        </li>
      </ul>
    </div>
  </section>

</body>
</html>
```